Vantrell Law Letterhead

We need a new letterhead design for a Law Firm. The address for the law firm is 4817 Larkspur Boulevard, Suite 250, Houston, Texas 77342. Phone Number: 832-619-3057; Fax Number: 832-407-1694. The logo is uploaded to the project.

```html
<!DOCTYPE html>
<html lang="en">
<head>
<meta charset="utf-8">
<title>Vantrell Law Letterhead</title>
<link rel="stylesheet" href="https://fonts.googleapis.com/css2?family=Figtree:wght@400;500;600&display=swap">
<style>
  :root {
    --backdrop: #dedede;
    --paper: #ffffff;
    --navy: #13224a;
    --red: #e01a22;
    --ink: #2b2b2b;
    --ink-soft: #3a3a3a;
  }
  * { margin: 0; padding: 0; box-sizing: border-box; }
  html, body {
    width: 1162px; height: 1200px; overflow: hidden;
    background: var(--backdrop);
    font-family: "Figtree", Arial, sans-serif;
  }
  .letterhead {
    position: absolute; left: 188px; top: 92px;
    width: 786px; height: 1018px;
    background: var(--paper);
    box-shadow: 0 2px 6px rgba(0,0,0,0.25);
    overflow: hidden;
  }
  .firm-name {
    position: absolute; left: 30px; top: 82px;
    font-size: 31px; font-weight: 600; letter-spacing: 0.5px;
    color: var(--navy);
  }
  .contact {
    position: absolute; left: 577px; top: 75px;
    border-left: 1.5px solid var(--red);
    padding-left: 19px; height: 88px;
    font-size: 13px; line-height: 15.5px; color: var(--ink);
  }
  .contact address { font-style: normal; }
  .contact-line {
    display: flex; align-items: center; gap: 10px;
    margin-top: 6px; line-height: 12px;
  }
  .contact address + .contact-line { margin-top: 8px; }
  .contact-line svg { width: 11px; height: 11px; fill: var(--red); }
  .recipient {
    position: absolute; left: 29px; top: 253px;
    font-size: 12.5px; line-height: 18px; color: var(--ink);
  }
  .letter-body {
    position: absolute; left: 31px; top: 331px; width: 727px;
    font-size: 12.4px; line-height: 18.1px; color: var(--ink-soft);
    text-align: justify; letter-spacing: 0.15px;
  }
  .letter-body p + p { margin-top: 18px; }
  .closing {
    position: absolute; left: 29px; top: 760px;
    font-size: 15px; color: var(--ink);
  }
  .signature {
    position: absolute; left: 27px; top: 787px;
    width: 88px; height: 25px; border-radius: 3px;
    background: linear-gradient(90deg, #e6e6e6, #f2f2f2);
  }
  .footer-wave {
    position: absolute; left: 0; bottom: 0;
    width: 786px; height: 158px;
  }
  .wave-red { fill: var(--red); }
  .wave-navy { fill: var(--navy); }
</style>
</head>
<body>
  <main class="letterhead">
    <header>
      <div class="firm-name">Vantrell Law</div>
      <div class="contact">
        <address>4817 Larkspur Boulevard,<br>Suite 250, Houston,<br>Texas 77342</address>
        <div class="contact-line">
          <svg viewBox="0 0 24 24" aria-hidden="true"><path d="M6.6 10.8a15 15 0 0 0 6.6 6.6l2.2-2.2a1 1 0 0 1 1-.25 11.4 11.4 0 0 0 3.6.57 1 1 0 0 1 1 1V20a1 1 0 0 1-1 1A17 17 0 0 1 3 4a1 1 0 0 1 1-1h3.5a1 1 0 0 1 1 1c0 1.25.2 2.45.57 3.57a1 1 0 0 1-.25 1z"/></svg>
          <span>832-619-3057</span>
        </div>
        <div class="contact-line">
          <svg viewBox="0 0 24 24" aria-hidden="true"><path d="M7 3h10v5H7zM4 9h16a2 2 0 0 1 2 2v6h-4v4H6v-4H2v-6a2 2 0 0 1 2-2zm4 7v3h8v-3z"/></svg>
          <span>832-407-1694</span>
        </div>
      </div>
    </header>

    <div class="recipient">
      Mr/s<br>First Name and Last Name<br>Company Name<br>Address
    </div>

    <section class="letter-body">
      <p>Lorem ipsum dolor sit amet,consectetur adipiscing sed do eiusmod tempor incididunt laboreet dolore magna aliqua.Ut enim ad minim.veniam, quis nostrud exercitation ullamco laboris nisi ut aliquip exea commodo consequat.Lorem ipsum dolor sit amet,consectetur adipiscing sed do eiusmod tempor incididunt.labore et dolore magna aliqua. Ut enim</p>
      <p>Lorem ipsum dolor sit amet, consectetur adipiscing sed do eiusmod tempor incididunt labore et dolore magna aliqua. Ut enim ad minim veniam, quis nostrud exercitation ullamco laboris nisi ut aliquip exea commodo consequat.Duis aute irure dolor in reprehenderit in voluptate velit esse cillum irure dolor in reprehenderit in voluptate velit esse irure</p>
      <p>Lorem ipsum dolor sit amet, consectetur adipiscing sed do eiusmod tempor incididunt labore et dolore magna aliqua. consequat. Duis aute irure dolor in.reprehenderit in voluptate velit esse cillum dolore eu fugiat nulla pariatur. Excepteur sint occaecat cupidatat non proident, sunt in culpa qui officia deserunt mollit,</p>
      <p>Lorem ipsum dolor sit amet, consectetur adipiscing sed do eiusmod tempor incididunt labore et dolore magna aliqua. Ut enim Lorem ipsum dolor sit amet, consectetur adipiscing sed do eiusmod tempor incididunt labore et dolore magna aliqua. Ut enim Lorem ipsum aliqua.ipsum</p>
      <p>Lorem ipsum dolor sit amet, consectetur adipiscing sed do eiusmod tempor incididunt labore et dolore magna aliqua. Ut enim ad minim veniam, quis nostrud exercitation ullamco laboris nisi ut aliquip exea commodo consequat.Duis aute irure dolor in reprehenderit in voluptate velit esse cillum irure dolor in reprehenderit in voluptate velit esse irure</p>
    </section>

    <div class="closing">Regards</div>
    <div class="signature" role="img" aria-label="Handwritten signature of the sender"></div>

    <svg class="footer-wave" viewBox="0 0 786 158" preserveAspectRatio="none" aria-hidden="true">
      <path class="wave-navy" d="M270 101 C450 95 650 60 786 10 L786 29 C650 66 450 99 270 101 Z"/>
      <path class="wave-red" d="M0 101 C200 112 450 110 786 37 L786 158 L0 158 Z"/>
    </svg>
  </main>
</body>
</html>
```